Health Benefits Association Website Design

The Allied Household Provision Association (AHPA) is an organization formed for the purpose of providing its members better value for selected health benefits and services. Members can use the association benefits either in conjunction with or independently of other medical insurance they may have. Some of the benefits available include discounted dental and vision care and prescription mail order services. There is no limitation on who can join. This membership will be primarily marketed as a way to enhance the value of a fixed benefit health insurance plan although members do not have to have the insurance plan join the association.

We are seeking a design for a website to be used for consumers to get information about membership and for current members to be able to access their benefits. The website should include:

1) A landing page to provide a description of the AHPA

2) A secondary page that can be duplicated that will:
a. Provide a list of benefits
b. Provide a membership enrollment form
c. Provide a member’s only access page
d. Provide a contact page for more information

We are seeking a modern but conservative design that will reflect value, simplicity and good health. The site design will also need to be compatible for use with mobile phones and tablets.

A copy of the association logo is included with the submission. It will also need to be incorporated into the website design. Layouts of similar association websites have also been included for reference.

Target Market(s)

Ages 25 to 65 unmarried, married with no children, professionals, self-employed, active and healthy

Industry/Entity Type

Health And Wellness

Number of Pages Required

2 page

Font styles to use
Sans Serif

Colors

Designer to choose colors to be used in the design.

Requirements
Must have
• AHPA Logo (attached). Use colors from the logo in the website design.
Nice to have
• Graphics, if used, should convey health and fitness and skew toward a diverse array of adults 25 to 40.

```html
<!DOCTYPE html>
<html lang="en">
<head>
<meta charset="utf-8">
<title>Allied Household Provision Association</title>
<link rel="stylesheet" href="https://fonts.googleapis.com/css2?family=Arimo:wght@400;700&family=Tinos:wght@400;700&display=swap">
<style>
:root{
  --olive:#8a9a4f;
  --olive-dark:#737758;
  --olive-text:#7e8f3e;
  --yellow:#f4c430;
  --page:#f4f4f4;
  --ink:#444;
  --ink-soft:#555;
  --rule:#c9c9c9;
  --white:#fff;
  --serif:"Tinos","Times New Roman",serif;
  --sans:"Arimo",Arial,sans-serif;
}
*{box-sizing:border-box;margin:0;padding:0}
html,body{width:1200px;height:2535px;overflow:hidden}
body{background:var(--page);font-family:var(--sans);color:var(--ink);position:relative}
.abs{position:absolute}
.top-line{left:0;top:0;width:1200px;height:5px;background:var(--olive)}
.brand{left:144px;top:30px;width:135px;height:176px;display:flex;align-items:center;justify-content:center;text-align:center;font-family:var(--serif);font-size:22px;line-height:1.2;color:var(--olive-text)}
.brand-circle{width:14px;height:14px;border-radius:50%;background:var(--yellow);margin:0 auto 8px}
.callout{left:825px;top:80px;display:flex;align-items:center;gap:14px}
.callout-label{font-family:var(--serif);font-size:16px;letter-spacing:1px;color:var(--olive-text)}
.callout-number{font-family:var(--serif);font-size:30px;color:#333;letter-spacing:1px;line-height:1.1}
.search{left:872px;top:155px;width:186px;height:38px;background:var(--white);border:1px solid #ddd;font-size:13px;color:#aaa;padding:11px 10px}
.search svg{position:absolute;right:8px;top:10px}
.hero{left:0;top:270px;width:1200px;height:594px;background:linear-gradient(100deg,#2f63b0 0%,#5a7fbf 8%,#e0c2ac 20%,#f0dcd0 38%,#ece8e4 55%,#c9c2bb 75%,#7f8590 100%)}
.nav{left:120px;top:238px;width:955px;height:53px;background:var(--olive-dark);border-bottom:5px solid var(--olive)}
.nav a{font-family:var(--serif);font-size:20px;color:var(--white);text-decoration:none;letter-spacing:.5px;position:absolute;top:12px}
.nav-social{position:absolute;right:14px;top:11px;display:flex;gap:12px}
.social-badge{width:29px;height:29px;border-radius:50%;background:var(--white);color:var(--olive-dark);font-family:var(--serif);font-size:14px;font-weight:700;display:flex;align-items:center;justify-content:center}
.social-badge.on{background:var(--yellow);color:var(--white)}
.dropdown{left:404px;top:291px;width:152px;background:var(--olive)}
.dropdown a{display:block;height:45px;line-height:45px;padding-left:12px;font-family:var(--serif);font-size:17px;color:var(--white);text-decoration:none;border-bottom:1px solid #9fae66}
.hero-title{left:565px;top:487px;width:481px;height:62px;background:var(--yellow);color:var(--white);font-weight:700;font-size:27px;padding:13px 17px;letter-spacing:.8px}
.hero-text{left:565px;top:549px;width:481px;height:131px;background:rgba(110,110,110,.88);color:var(--white);font-size:13.5px;line-height:20px;padding:16px 22px;letter-spacing:.7px}
.section-kicker{font-family:var(--serif);font-size:22px;color:#333;letter-spacing:1px}
.section-title{font-family:var(--serif);font-size:28px;letter-spacing:1.5px;color:#333}
.section-title em{font-style:normal;color:var(--olive-text)}
.rule{height:2px;background:var(--rule)}
.photo{border:3px solid #e2e2e2}
.body-text{font-size:14.5px;line-height:32px;color:var(--ink-soft);letter-spacing:.7px}
.body-text a{color:var(--olive-text);text-decoration:none}
.card-title{font-family:var(--serif);font-size:15px;letter-spacing:1px;color:#333}
.card-text{font-size:12.5px;line-height:17px;color:var(--ink-soft);width:296px;letter-spacing:.5px}
.btn{width:102px;height:31px;background:var(--olive-dark);color:var(--white);font-size:13px;text-align:center;line-height:31px;letter-spacing:.5px}
.quote{width:439px;height:140px;background:var(--white);border:1px solid #ddd}
.quote.yellow{border-bottom:6px solid var(--yellow)}
.quote.green{border-bottom:6px solid var(--olive)}
.avatar{left:12px;top:12px;width:110px;height:110px;border-radius:50%;border:5px solid #ddd}
.quote-mark{left:132px;top:12px;font-family:var(--serif);font-size:60px;color:#ddd;line-height:1}
.quote-text{left:140px;top:45px;width:285px;font-size:12.5px;line-height:16px;color:var(--ink-soft);letter-spacing:.4px}
.quote-name{right:18px;top:100px;font-size:12px;color:var(--ink-soft);letter-spacing:.5px}
.footer{left:0;top:2190px;width:1200px;height:308px;background:var(--olive-dark);color:var(--white)}
.footer-brand{left:144px;top:54px;width:130px;height:164px;display:flex;align-items:center;justify-content:center;text-align:center;font-family:var(--serif);font-size:20px;line-height:1.2}
.footer-brand .brand-circle{background:var(--white)}
.footer-text{left:330px;top:63px;width:310px;font-size:13.5px;line-height:16.5px;letter-spacing:.5px}
.footer-head{font-family:var(--serif);font-size:20px;letter-spacing:1.5px;padding-bottom:12px;border-bottom:1px solid #8e917a;width:200px}
.footer-list{list-style:none;margin-top:20px}
.footer-list li{font-family:var(--serif);font-size:15px;height:34.5px;display:flex;align-items:center;gap:10px;letter-spacing:.5px}
.dot{width:8px;height:8px;border-radius:50%;background:var(--white)}
.ring{width:18px;height:18px;border-radius:50%;background:var(--white);color:var(--olive-dark);font-family:var(--serif);font-size:11px;font-weight:700;display:flex;align-items:center;justify-content:center}
.copyright{left:0;top:2498px;width:1200px;height:37px;background:var(--olive);color:var(--white);font-family:var(--serif);font-size:15px;text-align:center;line-height:37px;letter-spacing:.5px}
</style>
</head>
<body>
<div class="abs top-line"></div>

<header>
  <div class="abs brand"><div><div class="brand-circle"></div>Allied Household Provision Association</div></div>
  <div class="abs callout">
    <svg width="40" height="40" viewBox="0 0 40 40" aria-hidden="true"><circle cx="20" cy="20" r="17" fill="none" stroke="var(--olive)" stroke-width="3"/><path d="M14 12c2-1 3 0 4 3l-2 2c1 3 3 5 5 6l2-2c3 1 4 2 3 4-1 2-3 3-6 1-4-2-7-6-8-10 0-2 1-3 2-4z" fill="var(--olive)"/></svg>
    <div><div class="callout-label">CALL US TOLL FREE:</div><div class="callout-number">12-4567-890</div></div>
  </div>
  <div class="abs search">Search keyword
    <svg width="18" height="18" viewBox="0 0 18 18" aria-hidden="true"><circle cx="10" cy="7" r="5.5" fill="none" stroke="#999" stroke-width="1.5"/><path d="M6 11l-5 5" stroke="#999" stroke-width="1.5"/></svg>
  </div>
</header>

<div class="abs hero" role="img" aria-label="Photo of a smiling woman in a dental chair with a dentist holding an instrument"></div>

<nav class="abs nav">
  <a style="left:28px">Home</a>
  <a style="left:145px">About us</a>
  <a style="left:292px">Benefits</a>
  <a style="left:437px">Our Services</a>
  <a style="left:620px">Contact us</a>
  <svg class="abs" style="left:63px;top:44px" width="14" height="8" aria-hidden="true"><path d="M0 8L7 0L14 8z" fill="var(--olive)"/></svg>
  <div class="nav-social">
    <span class="social-badge" title="Pagebook">P</span>
    <span class="social-badge on" title="Circles+">C</span>
    <span class="social-badge" title="Chirper">C</span>
    <span class="social-badge" title="Snapgram">S</span>
  </div>
</nav>
<div class="abs dropdown"><a>Demo Link</a><a>Demo Link</a><a style="border:0">Demo Link</a></div>

<div class="abs hero-title">Heading sample text goes here</div>
<div class="abs hero-text">Lorem ipsum dolor sit amet, consectetur adipiscing elit. Curabitur lacinia pretium risus ac euismod. Aliquam auctor convallis mattis. Maecenas ornare augue vel nibh molestie, nec ultrices velit tincidunt.</div>

<section>
  <div class="abs section-kicker" style="left:149px;top:910px">Welcome to</div>
  <div class="abs section-title" style="left:151px;top:940px;font-size:27px"><em>Allied Household Provision Association</em></div>
  <div class="abs rule" style="left:132px;top:985px;width:591px"></div>
  <div class="abs photo" style="left:160px;top:1024px;width:540px;height:289px;background:linear-gradient(180deg,#a9c8ea 0%,#7d9fcc 25%,#3f5f8f 50%,#b9ad94 72%,#4f6a3c 90%,#6b6b6b 100%)" role="img" aria-label="Photo of a modern glass office building"></div>
  <div class="abs body-text" style="left:160px;top:1343px;width:540px">
    <p>&nbsp;Lorem ipsum dolor sit amet, consectetur adipiscing elit. Fusce eget sem feugiat, <a>ullamcorper</a> nulla vitae, iaculis erat. Proin lacus magna, pharetra eget turpis in, imperdiet malesuada quam. Nunc accumsan ipsum metus, accumsan congue purus euismod sed.</p>
    <p style="margin-top:32px">Vivamus auctor tristique feugiat. Class aptent taciti sociosqu ad litora torquent per conubia nostra, <a>per inceptos himenaeos.</a> Fusce eu lacus ac nisi fringilla blandit. Aliquam et feugiat orci. Vestibulum laoreet suscipit turpis quis convallis. Maecenas bibendum quis ipsum eu accumsan.</p>
  </div>
</section>

<aside>
  <div class="abs section-title" style="left:771px;top:940px">Member’s <em>Benefits</em></div>
  <div class="abs rule" style="left:766px;top:985px;width:309px"></div>

  <div class="abs photo" style="left:769px;top:1024px;width:294px;height:183px;background:linear-gradient(110deg,#f3f3f3 0%,#dfe2e6 35%,#b7c4d6 65%,#6f86a8 100%)" role="img" aria-label="Photo of a doctor consulting an older patient"></div>
  <div class="abs card-title" style="left:769px;top:1227px">TITLE OF THIS LINK GOES HERE</div>
  <div class="abs card-text" style="left:769px;top:1251px">Lorem ipsum dolor sit amet, consectetur adipiscing elit. Curabitur lacinia pretium risus ac euismod. A ictor&nbsp; convallis mattis.</div>
  <div class="abs btn" style="left:771px;top:1313px">Read more</div>

  <div class="abs photo" style="left:771px;top:1404px;width:294px;height:183px;background:linear-gradient(110deg,#fbf6e9 0%,#e6e6e4 35%,#a9b3bf 65%,#4e5a6c 100%)" role="img" aria-label="Photo of a doctor examining a patient's knee"></div>
  <div class="abs card-title" style="left:771px;top:1607px">TITLE OF THIS LINK GOES HERE</div>
  <div class="abs card-text" style="left:771px;top:1631px">Lorem ipsum dolor sit amet, consectetur adipiscing elit. Curabitur lacinia pretium risus ac euismod. A ictor&nbsp; convallis mattis.</div>
  <div class="abs btn" style="left:773px;top:1693px">Read more</div>
</aside>

<section>
  <div class="abs section-title" style="left:149px;top:1752px">Memeber’s <em>Testimonials</em></div>
  <div class="abs rule" style="left:127px;top:1803px;width:943px"></div>
  <div class="abs body-text" style="left:152px;top:1835px;width:885px">Lorem ipsum dolor sit amet, consectetur adipiscing elit. Curabitur lacinia pretium risus ac euismod. A ictor&nbsp; convallis mattis. Maecenas ornare augue vel nibh molestie, nec ultrices velit tincidunt. Aliquam convallis mattis.Aliquam auctor Maecenas ornare augue vel nibh molestie, nec ultrices velit tincidunt.</div>

  <div class="abs quote yellow" style="left:144px;top:1962px">
    <div class="abs avatar" style="background:radial-gradient(circle at 50% 45%,#c69679 0%,#a87a5e 40%,#7a8a99 100%)" role="img" aria-label="Portrait photo of a smiling young man"></div>
    <div class="abs quote-mark">“</div>
    <div class="abs quote-text">Lorem ipsum dolor sit amet, consectetur adipiscing elit. Curabitur lacinia pretium risus ac euismod. A ictor&nbsp; convallis mattis.”</div>
    <div class="abs quote-name">- Sam Porter</div>
  </div>
  <div class="abs quote green" style="left:615px;top:1962px">
    <div class="abs avatar" style="background:radial-gradient(circle at 50% 45%,#f1d3bd 0%,#c98a5c 55%,#efeae4 100%)" role="img" aria-label="Portrait photo of a smiling woman"></div>
    <div class="abs quote-mark">“</div>
    <div class="abs quote-text">Lorem ipsum dolor sit amet, consectetur adipiscing elit. Curabitur lacinia pretium risus ac euismod. A ictor&nbsp; convallis mattis.”</div>
    <div class="abs quote-name">- Lena Marsh</div>
  </div>
</section>

<footer class="abs footer">
  <div class="abs footer-brand"><div><div class="brand-circle"></div>Allied Household Provision Association</div></div>
  <div class="abs footer-text">
    <p>Lorem ipsum dolor sit amet, consectetur adipiscing elit. Curabitur lacinia pretium risus ac euismod. A ictor&nbsp; convallis mattis. Maecenas ornare augue vel nibh molestie, nec ultrices velit tincidunt.</p>
    <p style="margin-top:16px">Aliquam convallis mattis.Aliquam auctor Maecenas ornare augue vel nibh molestie, nec ultrices velit tincidunt.</p>
  </div>
  <div class="abs" style="left:693px;top:46px">
    <div class="footer-head">QUICKLINKS</div>
    <ul class="footer-list">
      <li><span class="dot"></span>Home</li>
      <li><span class="dot"></span>About us</li>
      <li><span class="dot"></span>Member’s Benefits</li>
      <li><span class="dot"></span>Our Services</li>
      <li><span class="dot"></span>Contact us</li>
    </ul>
  </div>
  <div class="abs" style="left:921px;top:46px">
    <div class="footer-head" style="width:162px">SOCIAL MEDIA</div>
    <ul class="footer-list">
      <li><span class="ring">P</span>Pagebook</li>
      <li><span class="ring">C</span>Chirper</li>
      <li><span class="ring">S</span>Snapgram</li>
      <li><span class="ring">C</span>Circles+</li>
    </ul>
  </div>
</footer>
<div class="abs copyright">Copyright © 2017 Allied Household Provision Association.</div>
</body>
</html>
```